We need a fresh, new church business card!!

We need a church business card with basic info to hand out as invites. We are looking for something clean that communicates our basic information clearly.

We are open to square or rectangle card sizes.

General Public

Religious

The attached logo is the only one that I have available. We'd like to see options with with text of the logo lighter and on a dark background as well as options with white/light backgrounds.

Also, we'd like to see option with rounded corners.

• Address - 2718 Maple Row, Rockford, IL 61142
• Website - brookvane.example
• Phone - 815-555-0163
• Service times -
• Sunday - 10am Sunday School
• - 11am Family Worship
• - 6pm Night of Prayer
• Wednesday - 7:30pm Adult Bible Study
• Classes for all ages

```html
<!DOCTYPE html>
<html lang="en">
<head>
<meta charset="utf-8">
<title>Brookvane Pentecostal Church – Business Card</title>
<link rel="stylesheet" href="https://fonts.googleapis.com/css2?family=Open+Sans:wght@400;600;700&display=swap">
<style>
  :root {
    --stage: #3a3a3a;
    --card-dark: #050505;
    --card-light: #ffffff;
    --teal: #4f94a5;
    --text-light: #f2f2f2;
    --text-grey: #6d6d6d;
  }
  * { margin: 0; padding: 0; box-sizing: border-box; }
  html, body { width: 1200px; height: 900px; overflow: hidden; }
  body {
    background: var(--stage);
    font-family: "Open Sans", Arial, sans-serif;
    position: relative;
  }
  .card {
    position: absolute;
    width: 540px;
    height: 310px;
    border-radius: 26px;
    background: var(--card-dark);
    overflow: hidden;
    box-shadow: 0 18px 40px rgba(0,0,0,.45);
  }
  /* back side */
  .card--back { left: 60px; top: 110px; }
  .service {
    position: absolute;
    left: 48px;
    top: 118px;
    color: var(--text-light);
    font-size: 15px;
    line-height: 1.3;
  }
  .service__title {
    color: var(--teal);
    font-weight: 700;
    font-size: 15px;
    letter-spacing: .04em;
    margin-bottom: 6px;
  }
  .service__row { display: flex; gap: 14px; margin-bottom: 6px; }
  .service__day { color: var(--teal); font-weight: 600; width: 86px; }
  .back-brand {
    position: absolute;
    right: 40px;
    top: 54px;
    display: flex;
    align-items: center;
    gap: 14px;
    color: var(--text-light);
    font-weight: 700;
    font-size: 22px;
    letter-spacing: .06em;
  }
  .back-brand__dot {
    width: 56px; height: 56px; border-radius: 50%;
    background: var(--text-light);
  }
  /* front side */
  .card--front { left: 600px; top: 500px; }
  .front__band {
    position: absolute;
    left: 0; right: 0; bottom: 0;
    height: 112px;
    background: var(--card-light);
  }
  .front__accent {
    position: absolute;
    right: -40px;
    top: 150px;
    width: 130px; height: 130px;
    border-radius: 50%;
    background: var(--teal);
  }
  .brand {
    position: absolute;
    left: 150px;
    top: 72px;
    display: flex;
    align-items: center;
    gap: 16px;
  }
  .brand__dot { width: 46px; height: 46px; border-radius: 50%; background: var(--teal); }
  .brand__name {
    color: var(--text-light);
    font-weight: 600;
    font-size: 24px;
    letter-spacing: .05em;
    line-height: 1.1;
    text-transform: uppercase;
  }
  .brand__name small { display: block; font-size: 11px; letter-spacing: .22em; margin-top: 4px; }
  .person { position: absolute; left: 30px; top: 176px; }
  .person__name { color: var(--text-light); font-weight: 700; font-size: 21px; letter-spacing: .02em; }
  .person__role { color: var(--teal); font-size: 13px; font-weight: 600; letter-spacing: .06em; }
  .contact {
    position: absolute;
    left: 30px; bottom: 20px;
    color: var(--text-grey);
    font-size: 14px;
    line-height: 1.5;
  }
  .contact__item { display: flex; align-items: center; gap: 8px; }
  .contact__item svg { width: 12px; height: 12px; fill: var(--teal); }
  .address {
    position: absolute;
    left: 290px; bottom: 50px;
    color: var(--text-grey);
    font-size: 14px;
    line-height: 1.45;
  }
</style>
</head>
<body>
  <section class="card card--back" aria-label="Card back">
    <div class="back-brand"><span class="back-brand__dot"></span>BROOKVANE</div>
    <div class="service">
      <p class="service__title">SERVICE TIMES</p>
      <div class="service__row">
        <span class="service__day">Sunday:</span>
        <span>10am Sunday School<br>11am Family Worship<br>6pm Night of Prayer</span>
      </div>
      <div class="service__row">
        <span class="service__day">Wednesday:</span>
        <span>7:30pm Adult Bible Study<br>Classes for all ages</span>
      </div>
    </div>
  </section>

  <section class="card card--front" aria-label="Card front">
    <div class="front__band"></div>
    <div class="front__accent"></div>
    <div class="brand">
      <span class="brand__dot"></span>
      <p class="brand__name">Brookvane<small>Pentecostal Church</small></p>
    </div>
    <div class="person">
      <p class="person__name">MARA ELLISON</p>
      <p class="person__role">DIRECTOR</p>
    </div>
    <div class="contact">
      <p class="contact__item">
        <svg viewBox="0 0 24 24"><path d="M6.6 10.8a15 15 0 0 0 6.6 6.6l2.2-2.2a1 1 0 0 1 1-.25 11.4 11.4 0 0 0 3.6.57 1 1 0 0 1 1 1V20a1 1 0 0 1-1 1A17 17 0 0 1 3 4a1 1 0 0 1 1-1h3.5a1 1 0 0 1 1 1c0 1.25.2 2.45.57 3.57a1 1 0 0 1-.25 1z"/></svg>
        815-555-0163
      </p>
      <p class="contact__item">
        <svg viewBox="0 0 24 24"><circle cx="12" cy="12" r="10"/></svg>
        www.brookvane.example
      </p>
    </div>
    <p class="address">2718 Maple Row<br>Rockford, IL 61142</p>
  </section>
</body>
</html>
```